Massage Therapy and Personal Training Business Card (RT Restful)

I need a logo design based in Washington. The company is called RT Restful. RT are my initials. I specialize in massage therapy and personal training and general wellness of my clients. I've tried getting designs but haven't quite yet found what I'm looking for. I'm not inclined to a certain color yet but some color that resembles wellness such as light blue and white or green and white. Again, I'm not really picky about that. Thank you in advance

Industry/Entity Type

Business

Contact Information for Business Card

Have the description on one side and space for writing information on the back side such as number, appt, etc. I have an example attached. I see a lot of these card. I dont want the exact one, but something similar. Simple, professional and elegant.

Colors

Designer to choose colors to be used in the design.

Requirements
Must have
• Space on the back side to write
• A professional, elegant look
Should not have
• cartoon like style.

```html
<!DOCTYPE html>
<html lang="en">
<head>
<meta charset="utf-8">
<title>RT Restful — Business Card</title>
<link href="https://fonts.googleapis.com/css2?family=Questrial&family=Open+Sans:wght@400;700&display=swap" rel="stylesheet">
<style>
  :root {
    --backdrop: #e9e7e4;
    --card: #ffffff;
    --card-tint: #f4f4f3;
    --ink: #3a3a3a;
    --ink-strong: #1f1f1f;
    --rule: #9a9a9a;
    --accent-pink: #f28ad6;
    --accent-green: #b6d86c;
    --accent-orange: #f9a55b;
  }
  * { box-sizing: border-box; margin: 0; padding: 0; }
  html, body {
    width: 1200px;
    height: 844px;
    overflow: hidden;
  }
  body {
    background: var(--backdrop);
    font-family: "Open Sans", Arial, sans-serif;
    color: var(--ink);
    position: relative;
  }
  .card {
    position: absolute;
    top: 262px;
    width: 540px;
    height: 320px;
    background: var(--card);
    box-shadow: 0 6px 18px rgba(0,0,0,0.18);
  }
  .card--front { left: 40px; background: linear-gradient(135deg, var(--card-tint), var(--card)); }
  .card--back { left: 620px; }

  /* Front */
  .brand {
    position: absolute;
    top: 62px;
    right: 46px;
    display: flex;
    align-items: center;
    gap: 12px;
  }
  .brand__dot {
    width: 18px;
    height: 18px;
    border-radius: 50%;
    background: var(--accent-green);
  }
  .brand__name {
    font-family: "Questrial", "Century Gothic", sans-serif;
    font-size: 40px;
    color: var(--ink);
    letter-spacing: 0.5px;
  }
  .rule {
    position: absolute;
    height: 1px;
    background: var(--rule);
  }
  .rule--top { top: 126px; left: 230px; right: 40px; }
  .rule--mid { top: 166px; left: 150px; right: 40px; }
  .person {
    position: absolute;
    left: 40px;
    top: 196px;
  }
  .person__name {
    font-family: "Questrial", "Century Gothic", sans-serif;
    font-size: 17px;
    color: var(--ink-strong);
    letter-spacing: 0.3px;
  }
  .person__title {
    font-size: 12.5px;
    color: var(--ink);
  }
  .rule--person { top: 240px; left: 40px; right: 260px; }
  .address {
    position: absolute;
    left: 40px;
    top: 250px;
    font-size: 12.5px;
    color: var(--ink);
  }
  .contacts {
    position: absolute;
    left: 40px;
    right: 40px;
    top: 282px;
    display: flex;
    justify-content: space-between;
    font-size: 12.5px;
    color: var(--ink);
  }
  .contacts b { font-weight: 700; color: var(--ink-strong); }
  .contacts__web { font-weight: 700; color: var(--ink-strong); }

  /* Back */
  .back-mark {
    position: absolute;
    left: 70px;
    top: 70px;
    width: 120px;
    height: 120px;
    border-radius: 50%;
    background: var(--accent-pink);
    opacity: 0.85;
  }
  .write-line {
    position: absolute;
    left: 250px;
    right: 40px;
    height: 1px;
    background: var(--rule);
  }
  .write-line--1 { top: 120px; }
  .write-line--2 { top: 175px; }
  .write-line--3 { top: 230px; }
</style>
</head>
<body>
  <section class="card card--front" aria-label="Business card front">
    <div class="brand">
      <span class="brand__dot"></span>
      <span class="brand__name">RT Restful</span>
    </div>
    <div class="rule rule--top"></div>
    <div class="rule rule--mid"></div>
    <div class="person">
      <p class="person__name">DANIEL MORROW</p>
      <p class="person__title">Managing Director</p>
    </div>
    <div class="rule rule--person"></div>
    <p class="address">58 Cedar Lane, Olympia, WA, 98501</p>
    <div class="contacts">
      <span><b>P:</b> (360)555-0147</span>
      <span><b>E:</b> hello@rtrestful.com</span>
      <span class="contacts__web">www.rtrestful.com</span>
    </div>
  </section>

  <section class="card card--back" aria-label="Business card back with writing space">
    <div class="back-mark"></div>
    <div class="write-line write-line--1"></div>
    <div class="write-line write-line--2"></div>
    <div class="write-line write-line--3"></div>
  </section>
</body>
</html>
```